Kelvane Plumbing Business cards

Company is Kelvane Plumbing.
name Dashel Morrowby, I am a plumber, drainer, gasfitter and roofer
Mobile: 0431 906 154
Email address: info@kelvaneplumbing.example (check out my website for some ideas)
Website: www.kelvaneplumbing.example
ABN: 82 916 203 471
LIC: 604517K

I am reliable all round plumber. I am a 24 hour emergency service. Kelvane Plumbing is a professional plumbing service in the Illawarra, South Coast, Southern Sydney and Southern Highland regions of NSW. We offer a 24 hour emergency service for piece of mind to our customers. Call us now to see how we can help you. Kelvane Plumbing approaches every job with attention to detail and excellent customer service. With our superior workmanship you can be confident that the job will be done right the first time around. You can rest assured with results that are guaranteed to last.

Target Market(s)

the general public

Contact Information for Business Card

look up website for some ideas something with similar colours to logo and new modern and to catch the eye.

Colors
fdfdfd
ffffff
000000
7f7f7f
aaaaaa
33a6d7
0492cd

Requirements
Must have
• all contact details
• company- Kelvane Plumbing
• name- Dashel Morrowby
• number mobile- 0431 906 154
• Email address- info@kelvaneplumbing.example
• Website- www.kelvaneplumbing.example
• ABN- 82 916 203 471
• LIC- 604517K

```html
<!DOCTYPE html>
<html lang="en">
<head>
<meta charset="utf-8">
<title>Kelvane Plumbing – Business Cards</title>
<link rel="stylesheet" href="https://fonts.googleapis.com/css2?family=Arimo:wght@400;700&display=swap">
<style>
  :root {
    --blue: #1a9bcc;
    --blue-light: #33a6d7;
    --black: #040708;
    --white: #ffffff;
    --grey: #7f7f7f;
    --stage-center: #666666;
    --stage-edge: #2c2c2c;
  }
  * { margin: 0; padding: 0; box-sizing: border-box; }
  html, body { width: 1200px; height: 1200px; overflow: hidden; }
  body {
    position: relative;
    font-family: "Arimo", Arial, sans-serif;
    background: radial-gradient(circle at 42% 52%, var(--stage-center) 0%, #4a4a4a 45%, var(--stage-edge) 100%);
    color: var(--white);
  }

  .brand-mark {
    position: absolute;
    left: 40px; top: 112px;
    width: 290px;
    text-align: center;
    font-weight: 700;
    font-size: 30px;
    line-height: 1.15;
    color: var(--blue);
  }

  .card {
    position: absolute;
    background: var(--black);
    overflow: hidden;
    box-shadow: 0 2px 6px rgba(0,0,0,.35);
  }
  .card-front { left: 408px; top: 262px; width: 738px; height: 417px; }
  .card-back  { left: 408px; top: 723px; width: 736px; height: 415px; }

  .card-art { position: absolute; inset: 0; width: 100%; height: 100%; }

  .holder-name {
    position: absolute; left: 62px; top: 36px;
    font-size: 24px; font-weight: 700;
  }
  .holder-role {
    position: absolute; left: 62px; top: 70px;
    font-size: 11px;
  }

  .card-brand {
    position: absolute; left: 416px; top: 64px; width: 260px;
    text-align: right;
    font-size: 26px; font-weight: 700; line-height: 1.15;
    color: var(--blue);
  }

  .contact-list { list-style: none; position: absolute; left: 23px; top: 250px; }
  .contact-item {
    display: flex; align-items: center;
    height: 31px; margin-bottom: 20px;
    font-size: 17px; font-weight: 700; letter-spacing: .5px;
  }
  .contact-item.phone { font-size: 18px; letter-spacing: 4.6px; }
  .contact-icon {
    width: 30px; height: 30px; border-radius: 50%;
    background: var(--white);
    display: flex; align-items: center; justify-content: center;
    margin-right: 22px; flex: none;
  }
  .contact-icon svg { width: 18px; height: 18px; }

  .back-brand {
    position: absolute; left: 0; right: 0; top: 112px;
    text-align: center;
    font-size: 34px; font-weight: 700; line-height: 1.15;
    color: var(--blue);
  }
  .registration {
    position: absolute; left: 0; right: 0;
    text-align: center; font-size: 17px; font-weight: 700;
  }
  .registration.abn { top: 306px; }
  .registration.lic { top: 342px; }
</style>
</head>
<body>

  <div class="brand-mark">Kelvane<br>Plumbing</div>

  <section class="card card-front">
    <svg class="card-art" viewBox="0 0 923 521" preserveAspectRatio="none">
      <defs>
        <linearGradient id="pipe-tone" x1="0" y1="0" x2="1" y2="1">
          <stop offset="0" stop-color="#e6e6e6"/>
          <stop offset="1" stop-color="#bdbdbd"/>
        </linearGradient>
      </defs>
      <polygon points="0,0 490,0 923,507 923,521 910,521 0,143" fill="#1a9bcc" aria-hidden="true"/>
      <polygon points="456,0 492,0 923,492 923,521 900,521 440,240" fill="url(#pipe-tone)" role="img" aria-label="Illustration of a white water pipe with grey couplings bending across the card"/>
    </svg>

    <h1 class="holder-name">Dashel Morrowby</h1>
    <p class="holder-role">a plumber, drainer, gasfitter and roofer</p>

    <div class="card-brand">Kelvane<br>Plumbing</div>

    <ul class="contact-list">
      <li class="contact-item phone">
        <span class="contact-icon">
          <svg viewBox="0 0 24 24"><path fill="#1a9bcc" d="M6.6 10.8a15.2 15.2 0 0 0 6.6 6.6l2.2-2.2c.3-.3.7-.4 1-.2 1.1.4 2.3.6 3.6.6.6 0 1 .4 1 1V20c0 .6-.4 1-1 1A17 17 0 0 1 3 4c0-.6.4-1 1-1h3.5c.6 0 1 .4 1 1 0 1.3.2 2.5.6 3.6.1.3 0 .7-.2 1z"/></svg>
        </span>
        0431 906 154
      </li>
      <li class="contact-item">
        <span class="contact-icon">
          <svg viewBox="0 0 24 24"><rect x="3" y="6" width="18" height="12" fill="none" stroke="#1a9bcc" stroke-width="2"/><path d="M3 6l9 7 9-7M3 18l7-6M21 18l-7-6" fill="none" stroke="#1a9bcc" stroke-width="1.6"/></svg>
        </span>
        info@kelvaneplumbing.example
      </li>
      <li class="contact-item">
        <span class="contact-icon">
          <svg viewBox="0 0 24 24"><g fill="none" stroke="#1a9bcc" stroke-width="1.8"><circle cx="12" cy="12" r="9"/><ellipse cx="12" cy="12" rx="4" ry="9"/><path d="M3 12h18M4.5 7.5h15M4.5 16.5h15"/></g></svg>
        </span>
        www.kelvaneplumbing.example
      </li>
    </ul>
  </section>

  <section class="card card-back">
    <div class="back-brand">Kelvane<br>Plumbing</div>
    <p class="registration abn">ABN- 82 916 203 471</p>
    <p class="registration lic">LIC- 604517K</p>
  </section>

</body>
</html>
```